Kestrel Hitches Square Business Card Design

I would like a 2 x 2 square rounded corner business card.my business manufacture vehicle hitches and uses square tubing with rounded corners and would like to incorporate the border to look like the tubing...
4127 Larkfield Ave. Ashvale, Northmoor 40918
(731) 555-0187
dale@kestrelhitches.example
www.kestrelhitches.example

Target Market(s)

automotive / vehicle hitches

Industry/Entity Type

Automotive

Contact Information for Business Card

I would like a 2 x 2 square rounded corner business card.my business manufacture vehicle hitches and uses square tubing with rounded corners and would like to incorporate the border to look like the tubing... and red, white and blue theme colors

Font styles to use
Sans Serif

Colors

Designer to choose colors to be used in the design.

Requirements
Must have
• Boarder
Nice to have
• red, white, blue theme colors
Should not have
• odd colors

```html
<!DOCTYPE html>
<html lang="en">
<head>
<meta charset="utf-8">
<title>Kestrel Hitches – Square Business Card</title>
<link href="https://fonts.googleapis.com/css2?family=Open+Sans:wght@400;600;700&family=Arimo:wght@400&display=swap" rel="stylesheet">
<style>
  :root {
    --navy: #1d3f7a;
    --red: #e31b2e;
    --white: #ffffff;
    --bg-light: #c4c5c9;
    --bg-dark: #7f8085;
    --steel-dark: #5c5d61;
    --steel-mid: #a9aaae;
    --steel-light: #f2f2f3;
    --groove: #3f4043;
  }
  html, body {
    margin: 0;
    padding: 0;
    width: 1200px;
    height: 1000px;
    overflow: hidden;
  }
  body {
    position: relative;
    background: radial-gradient(ellipse at 50% 40%, var(--bg-light) 0%, #a3a4a8 45%, var(--bg-dark) 100%);
    font-family: "Arimo", Arial, sans-serif;
  }
  .card {
    position: absolute;
    top: 263px;
    width: 474px;
    height: 475px;
    border-radius: 74px;
    background:
      linear-gradient(90deg, var(--steel-dark) 0%, var(--steel-mid) 10%, #e6e6e8 18%, #8d8e92 30%, var(--steel-light) 48%, #9c9da1 62%, #e9e9ea 76%, #7b7c80 90%, var(--steel-dark) 100%);
    box-shadow: 0 10px 22px rgba(0,0,0,0.35);
  }
  .card--front { left: 108px; }
  .card--back { left: 618px; }
  .card__tube {
    position: absolute;
    inset: 30px;
    border-radius: 52px;
    border: 3px solid var(--groove);
    background:
      linear-gradient(180deg, #8a8b8f 0%, var(--steel-light) 14%, #a5a6aa 40%, #d9d9db 70%, #6f7074 100%);
    box-shadow: inset 0 0 10px rgba(0,0,0,0.35);
  }
  .card__face {
    position: absolute;
    inset: 27px;
    border-radius: 26px;
    background: var(--white);
    border: 4px solid #d5d6d8;
    box-shadow: 0 0 0 2px #8e8f93;
    text-align: center;
    color: var(--navy);
  }
  .brand {
    font-family: "Open Sans", Arial, sans-serif;
    font-weight: 600;
    color: var(--navy);
    margin: 0;
    line-height: 1.08;
  }
  .card--front .brand {
    font-size: 37px;
    padding-top: 50px;
  }
  .card--back .brand {
    font-size: 62px;
    padding-top: 145px;
  }
  .person__name {
    font-family: "Open Sans", Arial, sans-serif;
    font-weight: 700;
    font-size: 25px;
    margin: 18px 0 0;
    line-height: 1.2;
  }
  .person__role {
    font-family: "Open Sans", Arial, sans-serif;
    font-size: 19px;
    color: var(--red);
    margin: 0;
    line-height: 1.2;
  }
  .contact {
    margin: 16px 0 0;
    font-size: 19.5px;
    line-height: 24.3px;
    font-style: normal;
  }
  .contact a {
    color: inherit;
    text-decoration: none;
  }
</style>
</head>
<body>
  <section class="card card--front">
    <div class="card__tube">
      <div class="card__face">
        <p class="brand">Kestrel<br>Hitches</p>
        <p class="person__name">Dale R. Whitcombe</p>
        <p class="person__role">Owner</p>
        <address class="contact">
          4127 Larkfield Ave. Ashvale,<br>
          Northmoor 40918<br>
          (731) 555-0187<br>
          <a href="mailto:dale@kestrelhitches.example">dale@kestrelhitches.example</a><br>
          www.kestrelhitches.example
        </address>
      </div>
    </div>
  </section>

  <section class="card card--back">
    <div class="card__tube">
      <div class="card__face">
        <p class="brand">Kestrel<br>Hitches</p>
      </div>
    </div>
  </section>
</body>
</html>
```